I need a business card design for a real estate finance, development and management business. We deal with high net worth clients and ask that the business card be neat, clean and sophisticated. We like the attached logo design, font and color and want to incorporate all this into the business card.

Industry/Entity Type

Real Estate

```html
<!DOCTYPE html>
<html lang="en">
<head>
<meta charset="utf-8">
<title>Harbor Crest — Business Card</title>
<link rel="stylesheet" href="https://fonts.googleapis.com/css2?family=Cormorant+Garamond:wght@500;700&display=swap">
<style>
  :root {
    --board: #3a3a3a;
    --brand-blue: #1a78b4;
    --card-white: #ffffff;
    --serif: "Cormorant Garamond", Georgia, serif;
  }
  * { margin: 0; padding: 0; box-sizing: border-box; }
  html, body { width: 1200px; height: 847px; overflow: hidden; }
  body { background: var(--board); position: relative; font-family: var(--serif); color: var(--brand-blue); }

  .board-title {
    position: absolute; left: 0; width: 1200px; top: 88px;
    text-align: center; font-weight: 500; font-size: 86px; line-height: 1;
  }
  .rule { position: absolute; background: var(--brand-blue); }
  .brand-name {
    position: absolute; left: 0; width: 100%; text-align: center;
    font-family: var(--serif); font-weight: 500; color: var(--brand-blue);
    line-height: 1; white-space: nowrap;
  }
  .brand-name--board { top: 216px; width: 1200px; font-size: 92px; }

  .card {
    position: absolute; top: 467px; width: 366px; height: 203px;
    background: var(--card-white); border-radius: 22px; overflow: hidden;
  }
  .card--front { left: 171px; }
  .card--back { left: 662px; }
  .card--front .brand-name { top: 82px; font-size: 46px; }
  .card--back .brand-name { top: 26px; font-size: 52px; }

  .holder { position: absolute; left: 0; width: 176px; text-align: center; font-weight: 500; }
  .holder__name { top: 120px; font-size: 23px; line-height: 1; }
  .holder__role { top: 151px; font-size: 10px; }

  .contact-divider { position: absolute; top: 105px; width: 2px; height: 76px; background: var(--brand-blue); }
  .contact-icons { position: absolute; left: 182px; top: 107px; }
  .contact-list {
    position: absolute; left: 210px; top: 107px; list-style: none;
    font-weight: 700; font-size: 12px;
  }
  .contact-list li { height: 18.5px; line-height: 18.5px; white-space: nowrap; }
</style>
</head>
<body>

  <h1 class="board-title">Business Card</h1>
  <div class="rule" style="left:285px; top:200px; width:628px; height:4px;"></div>
  <div class="brand-name brand-name--board">Harbor Crest</div>

  <section class="card card--front" aria-label="Card front">
    <div class="rule" style="left:0; top:70px; width:366px; height:2px;"></div>
    <div class="brand-name">Harbor Crest</div>
    <div class="rule" style="left:0; top:129px; width:366px; height:2px;"></div>
  </section>

  <section class="card card--back" aria-label="Card back">
    <div class="rule" style="left:0; top:16px; width:366px; height:2px;"></div>
    <div class="brand-name">Harbor Crest</div>
    <div class="rule" style="left:0; top:86px; width:366px; height:2px;"></div>

    <div class="holder holder__name">Mark Ellis</div>
    <div class="holder holder__role">Administrator</div>

    <div class="contact-divider" style="left:176px;"></div>
    <div class="contact-divider" style="left:201px;"></div>

    <svg class="contact-icons" width="16" height="76" viewBox="0 0 16 76" aria-hidden="true">
      <g fill="none" stroke="#1a78b4" stroke-width="1.3">
        <rect x="4" y="2" width="8" height="13" rx="1.5"/>
        <circle cx="8" cy="50" r="6"/>
        <ellipse cx="8" cy="50" rx="2.6" ry="6"/>
        <line x1="2" y1="50" x2="14" y2="50"/>
      </g>
      <circle cx="8" cy="13" r="0.9" fill="#1a78b4"/>
      <circle cx="8" cy="31" r="6.5" fill="#1a78b4"/>
      <path d="M5.6 28.2 l1.3 -0.6 1 2 -0.9 0.7 c0.4 1 1 1.7 2 2.2 l0.7 -0.9 2 1 -0.6 1.4 c-2.8 0.2 -5.6 -2.9 -5.5 -5.8z" fill="#fff"/>
      <circle cx="8" cy="68" r="6.5" fill="#1a78b4"/>
      <text x="8" y="71" text-anchor="middle" font-size="9" font-family="Arial, sans-serif" fill="#fff">@</text>
    </svg>

    <ul class="contact-list">
      <li>(555) 010-2040</li>
      <li>1-555-010-2041</li>
      <li>www.harborcrest.com</li>
      <li>m.ellis@harborcrest.com</li>
    </ul>
  </section>

</body>
</html>
```